Corvane Alloys Collective Business Card

Design a business card for a new company. Corvane Alloys Collective is a subsidiary of KTP, Inc. (www.ktpreclaims.example)

Target Market(s)

B2B, Manufactures

Industry/Entity Type

Recycling

Contact Information for Business Card

Corvane Alloys Collective, LLC.
48217 North Wendlow Avenue
Alsip IL 60492
P: (312) 555-0143
F: (312) 555-0144
www.corvaneac.example
Email@corvaneac.example

Font styles to use
Sans Serif

Requirements
Must have
• A KTP, Inc. subsidiary company.
Nice to have
• Recycling Solutions. Uncompromised. (slogan)

```html
<!DOCTYPE html>
<html lang="en">
<head>
<meta charset="utf-8">
<title>Corvane Alloys Collective – Business Card</title>
<link rel="stylesheet" href="https://fonts.googleapis.com/css2?family=PT+Sans:wght@400;700&display=swap">
<style>
  :root {
    --page-bg: #e9eaec;
    --card-bg: #ffffff;
    --green: #2f6a24;
    --green-bright: #6f9e2c;
    --navy: #1d2a63;
    --text: #26305e;
  }
  html, body {
    margin: 0;
    padding: 0;
    width: 1200px;
    height: 970px;
    overflow: hidden;
    background: var(--page-bg);
    font-family: "PT Sans", sans-serif;
  }
  .card {
    position: absolute;
    left: 120px;
    top: 218px;
    width: 960px;
    height: 534px;
    background: var(--card-bg);
    border-radius: 16px;
    overflow: hidden;
    box-shadow: 0 10px 30px rgba(0,0,0,0.15);
  }
  .brand {
    position: absolute;
    left: 56px;
    top: 205px;
    width: 420px;
    display: flex;
    align-items: center;
    gap: 14px;
  }
  .brand-dot {
    width: 34px;
    height: 34px;
    border-radius: 50%;
    background: var(--green);
    flex: none;
  }
  .brand-name {
    font-size: 33px;
    font-weight: 700;
    color: var(--green);
    line-height: 1.1;
  }
  .details {
    position: absolute;
    left: 557px;
    top: 78px;
    color: var(--text);
    font-size: 23px;
    line-height: 30px;
  }
  .person-name {
    font-size: 30px;
    font-weight: 700;
    color: var(--green);
    line-height: 36px;
  }
  .person-role { margin-bottom: 14px; }
  .parent-company { margin-bottom: 4px; }
  .company-name { color: var(--green); }
  .contact-list {
    list-style: none;
    margin: 14px 0 0;
    padding: 0;
  }
  .contact-list li {
    display: flex;
    align-items: center;
    gap: 10px;
    line-height: 32px;
  }
  .contact-list svg { width: 20px; height: 20px; flex: none; }
  .footer-rule {
    position: absolute;
    left: 0;
    bottom: 46px;
    width: 100%;
    height: 6px;
    background: var(--green-bright);
  }
  .footer-band {
    position: absolute;
    left: 0;
    bottom: 0;
    width: 100%;
    height: 40px;
    background: var(--navy);
  }
</style>
</head>
<body>
  <div class="card">
    <div class="brand">
      <span class="brand-dot"></span>
      <span class="brand-name">Corvane Alloys Collective</span>
    </div>

    <div class="details">
      <div class="person-name">Dorian Kessler</div>
      <div class="person-role">Managing Director</div>
      <div class="parent-company">KTP, Inc</div>
      <div class="company-name">Corvane Alloys Collective, LLC.</div>
      <div>48217 North Wendlow Avenue</div>
      <div>Alsip IL 60492</div>
      <ul class="contact-list">
        <li>
          <svg viewBox="0 0 20 20"><path fill="var(--navy)" d="M2 8c0-3 4-5 8-5s8 2 8 5h-4V6H6v2zM5 9h10l2 8H3z"/><circle cx="10" cy="13" r="2" fill="#fff"/></svg>
          (312) 555-0143
        </li>
        <li>
          <svg viewBox="0 0 20 20"><rect x="5" y="2" width="10" height="5" fill="var(--navy)"/><rect x="2" y="8" width="16" height="7" rx="1" fill="var(--navy)"/><rect x="5" y="12" width="10" height="6" fill="var(--navy)" stroke="#fff" stroke-width="1.2"/></svg>
          (312) 555-0144
        </li>
        <li>
          <svg viewBox="0 0 20 20"><rect x="2" y="5" width="16" height="11" fill="var(--navy)"/><path d="M2 5l8 6 8-6" fill="none" stroke="#fff" stroke-width="1.4"/></svg>
          email@corvaneac.example
        </li>
        <li>
          <svg viewBox="0 0 20 20"><circle cx="10" cy="10" r="8" fill="var(--navy)"/><path d="M2 10h16M10 2c-3 3-3 13 0 16M10 2c3 3 3 13 0 16" fill="none" stroke="#fff" stroke-width="1.2"/></svg>
          www.corvaneac.example
        </li>
      </ul>
    </div>

    <div class="footer-rule"></div>
    <div class="footer-band"></div>
  </div>
</body>
</html>
```